Bluestone Nine LLC Flyer Design

Marketing Materials for Real Estate Company. This flyer will be used to promote the company throughout the Commercial Real Estate business in the United States. The team has been together for 15 years. We are the middle guys between the Tenant, Broker, and the Owner. In the case of working with a Franchisor, we will be their Plug and Play leasing arm that will assist their new Franchisee's with their site selection, lease negotiations, design and construction management.

Target Market(s)

Real Estate Owners, Franchisor's, and Brokers

Font styles to use
Serif

Colors

Designer to choose colors to be used in the design.

Requirements
Must have
• The flyer must have......
• 1. The Best Leasing Machine On The Planet
• 2. Over the past 15 years our group has completed 4,492 lease transactions resulting in leasing 17,803,114 square feet in shopping centers across the United States.
• 3. Plug and Play Leasing Specialists. We handle the details between when the broker shows up with the space and the tenant and completing the lease negotiations, legal negotiations and documentation, and construction management to Certificate of Occupancy.
• 4. For Information Call Colette Varga at 555-014-2763 or Wendy Falk at 555-017-8302.
Nice to have
• National Tenants the we have completed transactions with....
• Pellmart, Fresh Basket, Harbor Pams, Vexo, Dunn, QV Rendo, Burrasco, Pattersons, Wrap Shack, Brewhorns, Summit Workout, ShipVo, Tredwell, PKN, Halvorsons, Q&L, Ledger Union Bank, Hen Haus-O, Lotus Kitchen, Furvo, Dex-Mart, Fieldly, and Orbit Theaters

```html
<!DOCTYPE html>
<html lang="en">
<head>
<meta charset="utf-8">
<title>Bluestone Nine LLC Flyer</title>
<link rel="stylesheet" href="https://fonts.googleapis.com/css2?family=Montserrat:wght@400;500;600;700;800&display=swap">
<style>
:root{
  --green:#86c13f;
  --green-deep:#4f9a1e;
  --green-light:#a6d45a;
  --ink:#111111;
  --panel:#1c1c1e;
  --paper:#f6f8f7;
  --stage:#e4e6e5;
  --grey:#b5b7b8;
  --white:#ffffff;
}
*{margin:0;padding:0;box-sizing:border-box}
html,body{width:1120px;height:1200px;overflow:hidden;background:var(--stage);font-family:'Montserrat',sans-serif}
.flyer{position:absolute;left:140px;top:20px;width:840px;height:1160px;background:var(--paper);overflow:hidden;box-shadow:0 6px 24px rgba(0,0,0,.18)}
.brand{position:absolute;left:36px;top:46px;font-size:40px;font-weight:600;color:var(--green);letter-spacing:1px}
.hero{position:absolute;left:0;top:120px;width:840px;height:300px;background:linear-gradient(135deg,var(--green-light) 0%,var(--green) 45%,var(--green-deep) 100%)}
.hero-photo{position:absolute;right:0;top:0;width:520px;height:300px}
.headline{position:absolute;left:34px;top:30px;color:var(--white);text-shadow:0 2px 4px rgba(0,0,0,.35)}
.headline .lead{display:block;font-size:36px;font-weight:700;line-height:1.1}
.headline .big{display:block;font-size:62px;font-weight:800;line-height:1.04;letter-spacing:.5px}
.headline .tail{display:block;font-size:36px;font-weight:700;line-height:1.2}
.stats{position:absolute;left:0;top:420px;width:840px;height:72px;background:var(--green);color:var(--ink);font-size:15px;font-weight:600;text-align:center;line-height:1.35;padding-top:14px}
.about{position:absolute;left:20px;top:492px;width:345px;height:483px;background:var(--panel);border-radius:0 0 46px 46px}
.about-photo{position:absolute;left:38px;top:22px;width:270px;height:270px}
.about-text{position:absolute;left:18px;top:316px;width:310px;color:var(--green-light);font-size:14.5px;font-weight:500;text-align:center;line-height:1.3}
.contact{position:absolute;left:390px;top:540px;width:450px}
.contact h2{font-size:26px;font-weight:800;color:var(--ink);margin-left:12px}
.agent{position:absolute;left:0;width:450px;height:170px}
.agent svg{position:absolute;left:0;top:0}
.agent .name{position:absolute;left:185px;top:60px;font-size:27px;font-weight:800;color:var(--ink);white-space:nowrap}
.agent .phone{position:absolute;left:185px;top:98px;font-size:20px;font-weight:700;color:var(--ink)}
.agent-one{top:66px}
.agent-two{top:262px}
.tenants{position:absolute;left:0;top:1022px;width:840px;height:138px;background:var(--green)}
.tenants-tab{position:absolute;left:105px;top:996px;width:610px;height:44px}
.tenants-title{position:absolute;left:105px;top:1008px;width:610px;text-align:center;color:var(--green-light);font-size:16px;font-weight:700}
.tenant-list{position:absolute;left:40px;top:1060px;width:760px;text-align:center;color:var(--ink);font-size:16px;font-weight:600;line-height:1.35}
</style>
</head>
<body>
<main class="flyer">
  <div class="brand">Bluestone Nine LLC</div>

  <section class="hero">
    <svg class="hero-photo" viewBox="0 0 520 300" role="img" aria-label="Photo of a glass skyscraper seen from below">
      <defs>
        <linearGradient id="towerTone" x1="0" y1="0" x2="1" y2="1">
          <stop offset="0" stop-color="#2f4a5c"/>
          <stop offset=".5" stop-color="#8aa7b8"/>
          <stop offset="1" stop-color="#dfe9ee"/>
        </linearGradient>
      </defs>
      <polygon points="210,0 520,0 520,300 0,300" fill="url(#towerTone)"/>
    </svg>
    <h1 class="headline">
      <span class="lead">The Best</span>
      <span class="big">LEASING</span>
      <span class="big">MACHINE</span>
      <span class="tail">On The Planet</span>
    </h1>
  </section>

  <p class="stats">Over the past 15 years our group has completed 4,492 lease transactions resulting<br>in leasing 17,803,114 square feet in shopping centers across the United States.</p>

  <section class="about">
    <svg class="about-photo" viewBox="0 0 270 270" role="img" aria-label="Photo of a tall brick apartment building">
      <defs>
        <linearGradient id="brickTone" x1="0" y1="0" x2="1" y2="1">
          <stop offset="0" stop-color="#dfe4e6"/>
          <stop offset=".55" stop-color="#b0784f"/>
          <stop offset="1" stop-color="#6c7a3a"/>
        </linearGradient>
      </defs>
      <circle cx="135" cy="135" r="130" fill="url(#brickTone)" stroke="var(--green)" stroke-width="6"/>
    </svg>
    <p class="about-text">Plug and Play Leasing Specialists. We handle the details between when the broker shows up with the space and the tenant and completing the lease negotiations, legal negotiations and documentation, and construction management to Certificate of Occupancy.</p>
  </section>

  <section class="contact">
    <h2>For Information Call:</h2>
    <div class="agent agent-one">
      <svg width="450" height="170" viewBox="0 0 450 170" aria-hidden="true">
        <circle cx="85" cy="85" r="80" fill="var(--grey)" stroke="var(--ink)" stroke-width="6"/>
        <line x1="160" y1="132" x2="360" y2="132" stroke="var(--ink)" stroke-width="2"/>
        <circle cx="360" cy="132" r="5" fill="var(--ink)"/>
      </svg>
      <div class="name">Colette Varga</div>
      <div class="phone">555-014-2763</div>
    </div>
    <div class="agent agent-two">
      <svg width="450" height="170" viewBox="0 0 450 170" aria-hidden="true">
        <circle cx="85" cy="85" r="80" fill="var(--grey)" stroke="var(--ink)" stroke-width="6"/>
        <line x1="160" y1="132" x2="360" y2="132" stroke="var(--ink)" stroke-width="2"/>
        <circle cx="360" cy="132" r="5" fill="var(--ink)"/>
      </svg>
      <div class="name">Wendy Falk</div>
      <div class="phone">555-017-8302</div>
    </div>
  </section>

  <section class="tenants"></section>
  <svg class="tenants-tab" viewBox="0 0 610 44" aria-hidden="true">
    <polygon points="6,0 604,0 610,44 0,44" fill="var(--panel)"/>
  </svg>
  <div class="tenants-title">National Tenants the we have completed transactions with....</div>
  <p class="tenant-list">Pellmart, Fresh Basket, Harbor Pams, Vexo, Dunn, QV Rendo, Burrasco, Pattersons, Wrap Shack, Brewhorns, Summit Workout, ShipVo, Tredwell, PKN, Halvorsons, Q&amp;L, Ledger Union Bank, Hen Haus-O, Lotus Kitchen, Furvo, Dex-Mart, Fieldly, and Orbit Theaters</p>
</main>
</body>
</html>
```